New Business Card Design Project

I need a meaningful new business card. Therefore, the website should convey growth, joy, uniqueness, workout and a bit of luxury.
Color scheme should be petrol, gold and matching colors.

```html
<!DOCTYPE html>
<html lang="en">
<head>
<meta charset="utf-8">
<title>Core Circle Studio – Business Card</title>
<link href="https://fonts.googleapis.com/css2?family=Tinos:wght@400&family=Great+Vibes&display=swap" rel="stylesheet">
<style>
  :root {
    --backdrop: #5b5b5d;
    --gold-light: #ecc25e;
    --gold-mid: #d9aa3f;
    --gold-deep: #c0802f;
    --petrol-deep: #0e2e35;
    --petrol-mid: #15454f;
    --petrol-ink: #0b2a30;
    --text-light: #f2efe9;
    --rule: #6f8f94;
  }
  html, body {
    margin: 0;
    width: 1200px;
    height: 900px;
    overflow: hidden;
    background: var(--backdrop);
  }
  .canvas {
    position: relative;
    width: 1200px;
    height: 900px;
  }
  .card {
    position: absolute;
    width: 620px;
    height: 354px;
    overflow: hidden;
    box-shadow: 0 14px 30px rgba(0,0,0,.45);
  }

  /* Front */
  .card--front {
    left: 110px;
    top: 60px;
    border-radius: 40px 0 40px 0;
    background: radial-gradient(ellipse at 60% 45%, var(--gold-light) 0%, var(--gold-mid) 55%, var(--gold-deep) 100%);
    display: flex;
    align-items: center;
    justify-content: center;
  }
  .brand {
    display: flex;
    align-items: center;
    gap: 12px;
    font-family: "Tinos", "Times New Roman", serif;
    font-weight: 400;
    white-space: nowrap;
  }
  .brand__dot {
    width: 18px;
    height: 18px;
    border-radius: 50%;
    flex: none;
  }
  .brand__name {
    font-size: 34px;
    letter-spacing: 1px;
  }
  .card--front .brand { color: var(--petrol-ink); }
  .card--front .brand__dot { background: var(--petrol-ink); }

  /* Back */
  .card--back {
    left: 470px;
    top: 480px;
    border-radius: 0 40px 0 40px;
    background: radial-gradient(ellipse at 25% 40%, var(--petrol-mid) 0%, var(--petrol-deep) 70%);
    font-family: "Tinos", "Times New Roman", serif;
    color: var(--text-light);
  }
  .back__swoosh {
    position: absolute;
    inset: 0;
  }
  .back__ornament {
    position: absolute;
    right: 40px;
    top: 70px;
    width: 200px;
    height: 210px;
    border-radius: 40%;
    background: radial-gradient(ellipse at center, rgba(190,145,60,.28) 0%, rgba(190,145,60,0) 70%);
  }
  .back__identity {
    position: absolute;
    left: 34px;
    top: 66px;
    display: flex;
    align-items: center;
    gap: 14px;
    white-space: nowrap;
  }
  .back__name {
    font-family: "Great Vibes", cursive;
    font-size: 38px;
    line-height: 1;
    color: var(--gold-mid);
  }
  .back__divider {
    width: 1px;
    height: 26px;
    background: var(--gold-mid);
  }
  .back__role {
    font-size: 17px;
  }
  .contact-line {
    display: flex;
    align-items: center;
    gap: 10px;
    font-size: 16px;
    white-space: nowrap;
  }
  .contact-line svg {
    width: 16px;
    height: 16px;
    flex: none;
  }
  .back__phone {
    position: absolute;
    left: 40px;
    top: 130px;
  }
  .back__rule {
    position: absolute;
    left: 258px;
    top: 175px;
    width: 1px;
    height: 150px;
    background: var(--rule);
  }
  .back__brand {
    position: absolute;
    left: 30px;
    top: 230px;
    width: 215px;
  }
  .back__brand .brand { color: var(--gold-mid); gap: 10px; }
  .back__brand .brand__dot { background: var(--gold-mid); width: 14px; height: 14px; }
  .back__brand .brand__name { font-size: 22px; letter-spacing: .5px; }
  .back__details {
    position: absolute;
    left: 285px;
    top: 190px;
    display: flex;
    flex-direction: column;
    gap: 6px;
  }
  .back__address {
    font-size: 17px;
    line-height: 1.25;
    margin: 0 0 10px;
  }
</style>
</head>
<body>
<main class="canvas">

  <section class="card card--front" aria-label="Card front">
    <div class="brand">
      <span class="brand__dot"></span>
      <span class="brand__name">Core Circle Studio</span>
    </div>
  </section>

  <section class="card card--back" aria-label="Card back">
    <svg class="back__swoosh" viewBox="0 0 620 354" preserveAspectRatio="none" aria-hidden="true">
      <defs>
        <linearGradient id="swooshGold" x1="0" y1="0" x2="1" y2="1">
          <stop offset="0" stop-color="#b98a34"/>
          <stop offset=".5" stop-color="#f0c766"/>
          <stop offset="1" stop-color="#b7822e"/>
        </linearGradient>
      </defs>
      <path d="M330 0 L620 0 L620 300 C600 170 500 60 330 0 Z" fill="url(#swooshGold)"/>
      <path d="M360 0 C500 45 590 140 612 300" fill="none" stroke="#0e2e35" stroke-width="6"/>
      <path d="M330 0 C490 40 590 150 600 300" fill="none" stroke="#0e2e35" stroke-width="3"/>
    </svg>

    <div class="back__ornament" role="img" aria-label="Faint gold floral vine ornament"></div>

    <div class="back__identity">
      <span class="back__name">Lena Morgott</span>
      <span class="back__divider"></span>
      <span class="back__role">Pilates Trainer</span>
    </div>

    <div class="contact-line back__phone">
      <svg viewBox="0 0 24 24" aria-hidden="true"><path fill="#d9aa3f" d="M6.6 10.8a15 15 0 0 0 6.6 6.6l2.2-2.2c.3-.3.7-.4 1-.2 1.1.4 2.3.6 3.6.6.6 0 1 .4 1 1V20c0 .6-.4 1-1 1A17 17 0 0 1 3 4c0-.6.4-1 1-1h3.5c.6 0 1 .4 1 1 0 1.3.2 2.5.6 3.6.1.3 0 .7-.2 1z"/></svg>
      <span>+49 170 5550142</span>
    </div>

    <div class="back__brand">
      <div class="brand">
        <span class="brand__dot"></span>
        <span class="brand__name">Core Circle Studio</span>
      </div>
    </div>

    <div class="back__rule"></div>

    <div class="back__details">
      <p class="back__address">Lindenweg 12<br>83600 Seewald</p>
      <div class="contact-line">
        <svg viewBox="0 0 24 24" aria-hidden="true"><g fill="none" stroke="#d9aa3f" stroke-width="1.8"><circle cx="12" cy="12" r="9"/><path d="M3 12h18M12 3c3 3 3 15 0 18M12 3c-3 3-3 15 0 18"/></g></svg>
        <span>pilates-seewald.de</span>
      </div>
      <div class="contact-line">
        <svg viewBox="0 0 24 24" aria-hidden="true"><circle cx="12" cy="12" r="8" fill="none" stroke="#d9aa3f" stroke-width="2"/></svg>
        <span>corecircle_studio</span>
      </div>
      <div class="contact-line">
        <svg viewBox="0 0 24 24" aria-hidden="true"><g fill="none" stroke="#d9aa3f" stroke-width="1.8"><rect x="3" y="6" width="18" height="12"/><path d="M3 6l9 7 9-7"/></g></svg>
        <span>info@pilates-seewald.de</span>
      </div>
    </div>
  </section>

</main>
</body>
</html>
```